New homepage design www.quillharbor.nl

We need a new website design to go with our new designed logo.
We are a relativly small basketballclub that would like a shiny new webdesign for our homepage. We want te be able to create a real homepage/base for our clubmembers, where they can find news, upcoming events (agenda/calendar) and the related info on playing basketball at our club (games/tasks/teams and all).

The current website is located at: www.quillharbor.nl but is an outdated and not so appealing design.
There are no real designfeatures of the current site that have to be transferred to the new site.
Coding in HTML/CSS/JS/JPEG/PNG is enough, making a dynamic website will be my task. I just need the design in HTML (preferrably HTML 5)

There is not a huge budget, we are a club without a main sponsor.

Feel free to be creative and amaze us!

Text for the page in the new design will be created by us, you may use some sample text for filling.

Currently used pictures in the site don't have to be transferred to the new page (preferrably not!)
Updates

Tomorrow we will pick a design.

Industry/Entity Type

Events

Requirements
Must have
• The new logo as uploaded and attached.
News page.
Agenda page
HTML compatible same look and feel in all modern browsers (IE, FireFox, Chrome, Safari)
Nice to have
• HTML 5 validated and approved

```html
<!DOCTYPE html>
<html lang="en">
<head>
<meta charset="utf-8">
<title>Quillharbor Basketball</title>
<link href="https://fonts.googleapis.com/css2?family=Carlito:wght@400;700&display=swap" rel="stylesheet">
<style>
:root{
  --navy:#1e3249;
  --navy-deep:#172a3f;
  --band:#1a3550;
  --orange:#e6883a;
  --white:#ffffff;
  --grey-text:#555b63;
  --caption-bg:rgba(34,34,34,.92);
  --caption-text:#c8c8c8;
}
*{margin:0;padding:0;box-sizing:border-box}
html,body{width:1102px;height:1200px;overflow:hidden}
body{font-family:"Carlito",sans-serif;background:var(--navy);color:var(--white);position:relative}
.top-strip{position:absolute;top:0;left:0;width:100%;height:13px;background:var(--band)}
.header{position:absolute;top:13px;left:0;width:100%;height:94px;background:linear-gradient(#ffffff 0%,#ffffff 55%,#dfe3e8 100%)}
.brand{position:absolute;left:126px;top:32px;display:flex;align-items:center;gap:8px;color:var(--band);font-weight:700;font-size:26px}
.brand-dot{width:22px;height:22px;border-radius:50%;background:var(--band)}
.util-links{position:absolute;right:110px;top:25px;font-size:12.5px;color:var(--grey-text)}
.util-links span{margin:0 6px}
.nav{position:absolute;top:107px;left:0;width:100%;height:52px;background:linear-gradient(#2a4a68,#1a3550 60%,#18304a)}
.nav a{position:absolute;top:17px;font-size:16px;font-weight:700;color:var(--white);text-decoration:none}
.nav a.active{color:var(--orange)}
.search{position:absolute;left:766px;top:14px;width:226px;height:23px;background:#142a40;border-radius:2px;font-size:8.5px;color:#c7cfd8;padding:7px 8px}
.search svg{position:absolute;right:8px;top:6px}
.hero{position:absolute;top:159px;left:0;width:100%;height:397px;background:radial-gradient(ellipse at 45% 55%,#8a6a55 0%,#4d3e36 45%,#2a2420 100%)}
.arrow{position:absolute;top:168px}
.caption{position:absolute;left:687px;top:126px;width:276px;height:142px;background:var(--caption-bg);padding:16px 14px}
.caption h2{color:var(--orange);font-size:21px;font-weight:700;margin-bottom:6px}
.caption p{color:var(--caption-text);font-size:12px;line-height:19px}
.welcome{position:absolute;top:577px;left:0;width:100%;text-align:center}
.welcome h1{color:var(--orange);font-size:21px;font-weight:400;margin-bottom:4px}
.welcome p{font-size:12.5px;line-height:22px}
.col-title{position:absolute;top:737px;color:var(--orange);font-size:15.5px;font-weight:700}
.news-item{position:absolute;left:132px;width:250px}
.thumb{position:absolute;left:0;top:0;width:70px;height:61px}
.news-text{position:absolute;left:80px;top:-4px;width:175px}
.news-text h3{font-size:12.5px;line-height:17px;font-weight:700}
.news-text p{font-size:10px;line-height:16.5px}
.event{position:absolute;left:432px;top:787px;width:234px}
.event-img{width:234px;height:129px;background:linear-gradient(135deg,#8a5a4a,#5a3a36 60%,#9c8a7e)}
.event-date{font-size:12.5px;margin-top:15px}
.event h3{font-size:12.5px;line-height:17px;font-weight:700;margin-top:7px}
.event p{font-size:10px;line-height:16.5px;text-align:justify}
.teams{position:absolute;left:726px;top:782px;list-style:none}
.teams li{font-size:12.5px;height:25.8px;display:flex;align-items:center;gap:14px}
.teams li.active{color:var(--orange)}
.footer{position:absolute;top:1110px;left:0;width:100%;height:90px;background:var(--navy-deep)}
.footer-links{position:absolute;left:117px;top:25px;font-size:12.5px}
.footer-links span{margin:0 13px}
.copyright{position:absolute;left:117px;top:50px;font-size:12.5px}
.social{position:absolute;left:862px;top:27px;display:flex;gap:6px}
.social span{width:36px;height:36px;border-radius:50%;background:var(--white);display:block}
</style>
</head>
<body>
<div class="top-strip"></div>
<header class="header">
  <div class="brand"><span class="brand-dot"></span>Quillharbor</div>
  <div class="util-links">Links<span>|</span>Guestbook<span>|</span>Login</div>
</header>
<nav class="nav">
  <a class="active" style="left:149px" href="#">Home</a>
  <a style="left:223px" href="#">Teams</a>
  <a style="left:302px" href="#">Information</a>
  <a style="left:418px" href="#">Gallery</a>
  <a style="left:501px" href="#">Contact</a>
  <div class="search">Type search
    <svg width="10" height="10" viewBox="0 0 10 10"><circle cx="4" cy="4" r="3" fill="none" stroke="#aab5c0" stroke-width="1.4"/><line x1="6" y1="6" x2="9" y2="9" stroke="#aab5c0" stroke-width="1.6"/></svg>
  </div>
</nav>
<section class="hero" role="img" aria-label="Photo of two basketball players in a crowded arena">
  <svg class="arrow" style="left:80px" width="26" height="44" viewBox="0 0 26 44"><polyline points="22,3 5,22 22,41" fill="none" stroke="#cfcfcf" stroke-width="5"/></svg>
  <svg class="arrow" style="left:993px" width="26" height="44" viewBox="0 0 26 44"><polyline points="4,3 21,22 4,41" fill="none" stroke="#cfcfcf" stroke-width="5"/></svg>
  <div class="caption">
    <h2>Quillharbor</h2>
    <p>Lorem Ipsum is simply dummy text of the printing and typesetting industry. Lorem Ipsum has been the industry's standard dummy text ever since the 1500s</p>
  </div>
</section>
<section class="welcome">
  <h1>Welcome to quillharbor</h1>
  <p>The Board of BC Quill Harbor welcome you to our site.</p>
  <p>THANKS! Thank you all very much for the nice evening party!!! The cozy familiar atmosphere inside Quill Harbor has been present throughout the evening. Super!!</p>
  <p>Thank you all for coming, nice memories and fun! A special thanks to the organization of large Quill Harbor game. This was great!! Thank you!</p>
</section>
<h2 class="col-title" style="left:129px">Latest News</h2>
<h2 class="col-title" style="left:431px">Upcoming events</h2>
<h2 class="col-title" style="left:724px">Teams Info</h2>

<article class="news-item" style="top:787px">
  <div class="thumb" role="img" aria-label="Basketball game photo" style="background:linear-gradient(135deg,#3a2a3a,#6a5a3a)"></div>
  <div class="news-text"><h3>Lorem Ipsum is simply dummy text of the printing</h3><p>Lorem Ipsum has been the industry's standard dummy text ever since the 1500s, when an unknown .</p></div>
</article>
<article class="news-item" style="top:880px">
  <div class="thumb" role="img" aria-label="Basketball game photo" style="background:linear-gradient(135deg,#5a4a3e,#b0a496)"></div>
  <div class="news-text"><h3>Lorem Ipsum is simply dummy text of the printing</h3><p>Lorem Ipsum has been the industry's standard dummy text ever since the 1500s, when an unknown .</p></div>
</article>
<article class="news-item" style="top:981px">
  <div class="thumb" role="img" aria-label="Basketball game photo" style="background:linear-gradient(135deg,#1e2236,#5a4a6a)"></div>
  <div class="news-text"><h3>Lorem Ipsum is simply dummy text of the printing</h3><p>Lorem Ipsum has been the industry's standard dummy text ever since the 1500s, when an unknown .</p></div>
</article>

<article class="event">
  <div class="event-img" role="img" aria-label="Photo of a professional basketball game"></div>
  <p class="event-date">Event On : 24-12-2013</p>
  <h3>Lorem Ipsum is simply dummy text of the printing and typesetting industry.</h3>
  <p>Lorem Ipsum has been the industry's standard dummy text ever since the 1500s, when an unknown printer took a galley of type and scrambled it to make a type specimen book.</p>
</article>

<ul class="teams">
  <li class="active"><svg width="6" height="9" viewBox="0 0 6 9"><polyline points="1,1 5,4.5 1,8" fill="none" stroke="#fff" stroke-width="1.4"/></svg>Women Recreanten 1</li>
  <li><svg width="6" height="9" viewBox="0 0 6 9"><polyline points="1,1 5,4.5 1,8" fill="none" stroke="#fff" stroke-width="1.4"/></svg>Senior Women 1</li>
  <li><svg width="6" height="9" viewBox="0 0 6 9"><polyline points="1,1 5,4.5 1,8" fill="none" stroke="#fff" stroke-width="1.4"/></svg>Externals</li>
  <li><svg width="6" height="9" viewBox="0 0 6 9"><polyline points="1,1 5,4.5 1,8" fill="none" stroke="#fff" stroke-width="1.4"/></svg>Men Recreanten</li>
  <li><svg width="6" height="9" viewBox="0 0 6 9"><polyline points="1,1 5,4.5 1,8" fill="none" stroke="#fff" stroke-width="1.4"/></svg>Senior Men 1</li>
  <li><svg width="6" height="9" viewBox="0 0 6 9"><polyline points="1,1 5,4.5 1,8" fill="none" stroke="#fff" stroke-width="1.4"/></svg>Senior Men 2</li>
  <li><svg width="6" height="9" viewBox="0 0 6 9"><polyline points="1,1 5,4.5 1,8" fill="none" stroke="#fff" stroke-width="1.4"/></svg>Boys Under 14</li>
  <li><svg width="6" height="9" viewBox="0 0 6 9"><polyline points="1,1 5,4.5 1,8" fill="none" stroke="#fff" stroke-width="1.4"/></svg>Boys Under 16</li>
  <li><svg width="6" height="9" viewBox="0 0 6 9"><polyline points="1,1 5,4.5 1,8" fill="none" stroke="#fff" stroke-width="1.4"/></svg>Boys Under 18</li>
  <li><svg width="6" height="9" viewBox="0 0 6 9"><polyline points="1,1 5,4.5 1,8" fill="none" stroke="#fff" stroke-width="1.4"/></svg>Girls Under 14</li>
  <li><svg width="6" height="9" viewBox="0 0 6 9"><polyline points="1,1 5,4.5 1,8" fill="none" stroke="#fff" stroke-width="1.4"/></svg>Quill Harbor</li>
</ul>

<footer class="footer">
  <div class="footer-links">Home<span>|</span>Teams<span>|</span>Information<span>|</span>Gallery<span>|</span>Contact</div>
  <div class="copyright">Copyright © 2013 All rights Reserved</div>
  <div class="social" aria-label="Social media links"><span></span><span></span><span></span></div>
</footer>
</body>
</html>
```